Infographic about trade negotiations and digital rights

There are a variety of trade negotiations, both current and future, that affect Internet users in various ways. But these are very confusing, because of the number of such agreements, the different parties that they include, and the different issues that they include. We want to create an infographic that simplifies this and makes it easier to understand the landscape of these trade agreements at a glance.

Target Market(s)

Informed audience of intelligent citizens and professionals

Industry/Entity Type

Non-Profit

Colors
ec1f27
000000

Requirements
Must have
• I will work with you on the exact text and data for the infographic. For now I am only interested in seeing mock-ups of the visual design. For this, you should include the following mock data:
• (a) Trade agreements called GLW, CUMEL, DYOB, MLSZ, BOVE, VelAD, ZEMO
• (b) Colour-coded issues grouped into the following categories: IP (sub-issues: copyright term, criminal enforcement, civil enforcement, DRM, trade secrets, broadcasting), e-commerce (sub-issues: source code, data localization, safe harbors, data flows, net neutrality, crypto, domain names), other (sub-issues: ISDS, telecommunications)
• (c) Parties to trade agreements: Europe, OLDIV, China, India, United States, Australia, New Zealand, Mexico, Canada, Chile, Peru
• The infographic will show how these agreements intersect. For example, CUMEL might have all of the ISSUES except for broadcasting and all of the PARTIES except for Europe. Whereas BOVE might not include any of the IP issues and does include Europe. For now, you can just make up the intersections. They don't have to be real.
• Also include our logo somewhere.
Nice to have
• Ideally should fit nicely onto a single full page of US Letter size paper.

```html
<!DOCTYPE html>
<html lang="en">
<head>
<meta charset="utf-8">
<title>Global Trade Agreements Review</title>
<link rel="stylesheet" href="https://fonts.googleapis.com/css2?family=Carlito:wght@400;700&display=swap">
<style>
  :root {
    --red: #ec1f27;
    --black: #000000;
    --white: #ffffff;
    --ink: #1a1a1a;
    --night: #15183a;
    --night-deep: #0b0d22;
    --box-line: #2a2a2a;
  }
  * { box-sizing: border-box; margin: 0; padding: 0; }
  html, body { width: 1200px; height: 900px; overflow: hidden; background: var(--white); }
  body { font-family: "Carlito", "Calibri", sans-serif; }

  .infographic { position: relative; width: 1200px; height: 900px; overflow: hidden; background: var(--white); }

  .title-bar {
    position: absolute; left: 0; top: 0; width: 1200px; height: 78px;
    background: var(--black);
  }
  .title-bar h1 {
    position: absolute; left: 44px; top: 20px;
    color: var(--white); font-size: 34px; font-weight: 700; line-height: 1;
  }

  .world-map {
    position: absolute; left: 0; top: 92px; width: 1200px; height: 720px;
    background: radial-gradient(ellipse 62% 58% at 50% 48%, var(--night) 0%, var(--night-deep) 62%, rgba(255,255,255,0) 82%);
  }

  .key-list { position: absolute; list-style: none; width: 265px; }
  .key-list.issues { left: 30px; top: 101px; }
  .key-list.parties { left: 900px; top: 101px; }
  .key-list li {
    height: 30px; margin-bottom: 10px;
    border: 1.5px solid var(--box-line); border-radius: 3px;
    background: var(--white); color: var(--red);
    font-size: 20px; line-height: 27px; padding-left: 8px;
    white-space: nowrap;
  }
  .key-list li.group-head {
    background: var(--red); color: var(--white); font-weight: 700;
  }

  .agreement-chart { position: absolute; left: 450px; top: 90px; width: 300px; height: 740px; }
  .agreement-chart .oval { fill: url(#ovalShade); stroke: #b8141b; stroke-width: 1; }
  .agreement-chart .oval-label { fill: var(--white); font-family: "Carlito", sans-serif; font-weight: 700; font-size: 30px; text-anchor: middle; dominant-baseline: central; }
  .agreement-chart .tag { fill: var(--white); stroke: var(--red); stroke-width: 1.3; }
  .agreement-chart .tag-num { fill: var(--ink); font-family: "Carlito", sans-serif; font-size: 11px; font-weight: 700; text-anchor: middle; dominant-baseline: central; }

  .footer-rule { position: absolute; left: 0; top: 838px; width: 1200px; height: 3px; background: var(--black); }
  .sponsor {
    position: absolute; left: 0; top: 852px; width: 1200px; height: 36px;
    display: flex; align-items: center; justify-content: center; gap: 14px;
  }
  .sponsor-mark { width: 34px; height: 34px; background: var(--black); }
  .sponsor-name { font-size: 21px; font-weight: 400; letter-spacing: 1.5px; color: var(--black); text-transform: uppercase; }
  .sponsor-site { font-size: 19px; color: var(--red); margin-left: 18px; }
</style>
</head>
<body>
<main class="infographic">
  <header class="title-bar"><h1>Global Trade Agreements Review</h1></header>

  <div class="world-map" role="img" aria-label="Dark night-sky world map with continents behind the chart"></div>

  <ul class="key-list issues">
    <li class="group-head">IP</li>
    <li>1. Copyright term</li>
    <li>2. Criminal enforcement</li>
    <li>3. Civil enforcement</li>
    <li>4. DRM</li>
    <li>5. Trade secrets</li>
    <li>6. Broadcasting</li>
    <li class="group-head">E-Commerce</li>
    <li>7. Source code</li>
    <li>8. Data localization</li>
    <li>9. Safe harbors</li>
    <li>10. Data flows</li>
    <li>11. Net neutrality</li>
    <li>12. Crypto</li>
    <li>13. Domain names</li>
    <li class="group-head">Other</li>
    <li>14. ISDS</li>
    <li>15. Telecommunications</li>
  </ul>

  <ul class="key-list parties">
    <li>1. Europe</li>
    <li>2. OLDIV</li>
    <li>3. China</li>
    <li>4. India</li>
    <li>5. United States</li>
    <li>6. Australia</li>
    <li>7. New Zealand</li>
    <li>8. Mexico</li>
    <li>9. Canada</li>
    <li>10. Chile</li>
    <li>11. Peru</li>
  </ul>

  <svg class="agreement-chart" viewBox="0 0 300 740" width="300" height="740" aria-label="Agreements with their issue and party numbers">
    <defs>
      <radialGradient id="ovalShade" cx="50%" cy="40%" r="60%">
        <stop offset="0%" stop-color="#f2373e"/>
        <stop offset="100%" stop-color="#d81a21"/>
      </radialGradient>
      <g id="tags">
        <circle class="tag" cx="-111" cy="-29" r="10"/><text class="tag-num" x="-111" y="-29">2</text>
        <circle class="tag" cx="-88" cy="-29" r="10"/><text class="tag-num" x="-88" y="-29">10</text>
        <circle class="tag" cx="-99" cy="-10" r="10"/><text class="tag-num" x="-99" y="-10">12</text>
        <circle class="tag" cx="-120" cy="0" r="10"/><text class="tag-num" x="-120" y="0">5</text>
        <circle class="tag" cx="-100" cy="14" r="10"/><text class="tag-num" x="-100" y="14">1</text>
        <circle class="tag" cx="-110" cy="34" r="10"/><text class="tag-num" x="-110" y="34">8</text>
        <circle class="tag" cx="-88" cy="32" r="10"/><text class="tag-num" x="-88" y="32">3</text>
        <circle class="tag" cx="90" cy="-30" r="10"/><text class="tag-num" x="90" y="-30">1</text>
        <circle class="tag" cx="99" cy="-10" r="10"/><text class="tag-num" x="99" y="-10">12</text>
        <circle class="tag" cx="99" cy="11" r="10"/><text class="tag-num" x="99" y="11">10</text>
        <circle class="tag" cx="94" cy="31" r="10"/><text class="tag-num" x="94" y="31">3</text>
      </g>
    </defs>
    <g transform="translate(148 54)"><use href="#tags"/><ellipse class="oval" rx="81" ry="39"/><text class="oval-label">GLW</text></g>
    <g transform="translate(148 159)"><use href="#tags"/><ellipse class="oval" rx="81" ry="39"/><text class="oval-label">CUMEL</text></g>
    <g transform="translate(148 264)"><use href="#tags"/><ellipse class="oval" rx="81" ry="39"/><text class="oval-label">DYOB</text></g>
    <g transform="translate(148 369)"><use href="#tags"/><ellipse class="oval" rx="81" ry="39"/><text class="oval-label">MLSZ</text></g>
    <g transform="translate(148 474)"><use href="#tags"/><ellipse class="oval" rx="81" ry="39"/><text class="oval-label">BOVE</text></g>
    <g transform="translate(148 579)"><use href="#tags"/><ellipse class="oval" rx="81" ry="39"/><text class="oval-label">VelAD</text></g>
    <g transform="translate(148 684)"><use href="#tags"/><ellipse class="oval" rx="81" ry="39"/><text class="oval-label">ZEMO</text></g>
  </svg>

  <div class="footer-rule"></div>
  <footer class="sponsor">
    <span class="sponsor-mark"></span>
    <span class="sponsor-name">Open Signal Alliance</span>
    <span class="sponsor-site">opensignal.example</span>
  </footer>
</main>
</body>
</html>
```